Brell Harbor Company Business Cards

Front and Back Business Card - logo and text setup - cool design. I need workable photoshop or illustrator files so I can setup each employee card with design that is created
Updates

Hi everyone, thank you for the great entries. Please no more white and blue cards - there are so many already - black and silver only now please. thanks!

Target Market(s)

Construction Industry - Facility Managers

Industry/Entity Type

Construction

Contact Information for Business Card

I really like contemporary simplistic looks - clean neat....not opposed to seeing some black backrounds

Requirements
Must have
• Logo/website address with design on front only - www.brellharbor-example.com (logo attached)
• Back:
• Name/Title/Company Address/Phone/email address
Nice to have
• Cool design
Should not have
• Nothing gimmicky like Fire or Water - since we are a Fire Protection company - it has all been done

```html
<!DOCTYPE html>
<html lang="en">
<head>
<meta charset="utf-8">
<title>Brell Harbor Company – Business Cards</title>
<link href="https://fonts.googleapis.com/css2?family=Titillium+Web:wght@300;400;600;700&display=swap" rel="stylesheet">
<style>
  :root {
    --page: #ffffff;
    --label: #111111;
    --card-top: #2b2b2d;
    --card-bottom: #050506;
    --white: #ffffff;
    --silver: #c9c9cc;
    --silver-dim: #8d8d91;
    --name-bold: #a9a9ad;
    --name-light: #d2d2d5;
  }
  * { margin: 0; padding: 0; box-sizing: border-box; }
  html, body { width: 1200px; height: 1200px; overflow: hidden; background: var(--page); }
  .sheet { position: relative; width: 1200px; height: 1200px; }
  .side-label {
    position: absolute; top: 428px; width: 300px; margin-left: -150px;
    text-align: center; font: 400 35px/1 Arial, Helvetica, sans-serif; color: var(--label);
  }
  .side-label--front { left: 280px; }
  .side-label--back { left: 921px; }
  .card {
    position: absolute; top: 489px; width: 487px; height: 278px;
    background: linear-gradient(to bottom, var(--card-top) 0%, #1a1a1c 40%, var(--card-bottom) 100%);
    font-family: "Titillium Web", sans-serif; color: var(--white); overflow: hidden;
  }
  .card--front { left: 37px; }
  .card--back { left: 678px; }
  .card-frames { position: absolute; inset: 0; }
  .wordmark { position: absolute; font-weight: 700; color: var(--white); letter-spacing: -0.5px; white-space: nowrap; }
  .card--front .wordmark { left: 0; width: 100%; top: 112px; text-align: center; font-size: 40px; line-height: 1; }
  .website {
    position: absolute; left: 0; width: 100%; top: 224px; text-align: center;
    font-size: 15px; letter-spacing: 3.2px; font-weight: 400; color: var(--white);
  }
  .card--back .wordmark { right: 42px; top: 32px; font-size: 21px; line-height: 1; }
  .holder-name { position: absolute; left: 41px; top: 36px; font-size: 27px; line-height: 1; letter-spacing: 0.3px; }
  .holder-name b { font-weight: 700; color: var(--name-bold); }
  .holder-name span { font-weight: 300; color: var(--name-light); }
  .name-rule {
    position: absolute; left: 41px; top: 69px; width: 212px; height: 1px;
    background: linear-gradient(to right, var(--silver) 0%, var(--silver-dim) 70%, rgba(141,141,145,0) 100%);
  }
  .holder-title { position: absolute; left: 41px; top: 73px; font-size: 18px; font-weight: 300; color: var(--name-light); }
  .contact-list { position: absolute; left: 41px; top: 177px; list-style: none; }
  .contact-list li { display: flex; align-items: center; height: 14px; font-size: 11px; font-weight: 400; color: #d6d6d8; }
  .contact-list svg { width: 8px; height: 8px; margin-right: 7px; flex: none; fill: #d6d6d8; }
</style>
</head>
<body>
<main class="sheet">
  <div class="side-label side-label--front">FRONT</div>
  <div class="side-label side-label--back">BACK</div>

  <section class="card card--front" aria-label="Business card front">
    <svg class="card-frames" width="487" height="278" viewBox="0 0 487 278" aria-hidden="true">
      <defs>
        <linearGradient id="frontShine" x1="0" y1="0" x2="1" y2="0">
          <stop offset="0" stop-color="#6e6e72"/>
          <stop offset="0.25" stop-color="#f2f2f4"/>
          <stop offset="0.5" stop-color="#9a9a9e"/>
          <stop offset="0.8" stop-color="#f2f2f4"/>
          <stop offset="1" stop-color="#6e6e72"/>
        </linearGradient>
      </defs>
      <rect x="18" y="16" width="451" height="243" fill="none" stroke="#8a8a8e" stroke-width="2.5"/>
      <rect x="26" y="12" width="448" height="242" fill="none" stroke="#6c6c70" stroke-width="1.5"/>
      <line x1="18" y1="16" x2="469" y2="16" stroke="url(#frontShine)" stroke-width="2.5"/>
      <line x1="18" y1="259" x2="469" y2="259" stroke="url(#frontShine)" stroke-width="2.5"/>
    </svg>
    <div class="wordmark">brellharbor</div>
    <div class="website">www.brellharbor-example.com</div>
  </section>

  <section class="card card--back" aria-label="Business card back">
    <svg class="card-frames" width="487" height="278" viewBox="0 0 487 278" aria-hidden="true">
      <defs>
        <linearGradient id="backShine" x1="0" y1="0" x2="1" y2="0">
          <stop offset="0" stop-color="#6e6e72"/>
          <stop offset="0.3" stop-color="#f2f2f4"/>
          <stop offset="0.55" stop-color="#9a9a9e"/>
          <stop offset="0.85" stop-color="#f2f2f4"/>
          <stop offset="1" stop-color="#6e6e72"/>
        </linearGradient>
      </defs>
      <rect x="15" y="21" width="451" height="242" fill="none" stroke="#8a8a8e" stroke-width="2.5"/>
      <rect x="23" y="16" width="448" height="242" fill="none" stroke="#6c6c70" stroke-width="1.5"/>
      <line x1="15" y1="21" x2="466" y2="21" stroke="url(#backShine)" stroke-width="2.5"/>
      <line x1="15" y1="263" x2="466" y2="263" stroke="url(#backShine)" stroke-width="2.5"/>
    </svg>
    <h1 class="holder-name"><b>YOUR</b> <span>NAME</span></h1>
    <div class="name-rule"></div>
    <p class="holder-title">Your Job Title</p>
    <div class="wordmark">brellharbor</div>
    <ul class="contact-list">
      <li><svg viewBox="0 0 10 10"><path d="M5 0a3.5 3.5 0 0 0-3.5 3.5C1.5 6 5 10 5 10s3.5-4 3.5-6.5A3.5 3.5 0 0 0 5 0zm0 5a1.5 1.5 0 1 1 0-3 1.5 1.5 0 0 1 0 3z"/></svg>48 Quarry Lane, Westbrook, NY 11900</li>
      <li><svg viewBox="0 0 10 10"><path d="M2 0l2 2.5-1 1.3c.6 1.3 1.7 2.4 3 3L7.4 6 10 8l-1 1.6C4.5 10 0 5.5.4 1z"/></svg>Tell: (555) 014-2760</li>
      <li><svg viewBox="0 0 10 10"><path d="M2.5 0h4l1 1v2h-5zM0 4h10v4H8v2H2V8H0zm3 3v2h4V7z"/></svg>Fax: (555) 014-2761</li>
      <li><svg viewBox="0 0 10 10"><path d="M5 0a5 5 0 1 0 2.5 9.3l-.5-.9A4 4 0 1 1 9 5v.6c0 .7-.4 1-.8 1s-.7-.3-.7-1V2.8h-1v.5A2.5 2.5 0 1 0 6.7 7a1.7 1.7 0 0 0 3.3-1.4V5a5 5 0 0 0-5-5zm0 6.5a1.5 1.5 0 1 1 0-3 1.5 1.5 0 0 1 0 3z"/></svg>info@brellharbor-example.com</li>
      <li><svg viewBox="0 0 10 10"><circle cx="5" cy="5" r="3"/></svg>social page</li>
    </ul>
  </section>
</main>
</body>
</html>
```